I am a health and wellness guru. I am looking to make a website. Nothing too extensive but something to just promote on my socials and sell the info I know as digital assets. I will sell my daily workout as a monthly payment, and they will get updates on what I do daily... As well as a pdf of my day and a guide to a healthy lifestyle. I may offer meal plans and coaching as well. It will be called a venture brightpath and then offer those things. my Instagram @marlon_tibbet you can see kinda my vibe off stuff. I want a clean aesthetic look and simple. Whatever photos you reccoment ill provide when I pick a winning design

Target Market(s)

people who want to buy access to my way of life

Coding

Font styles to use
Serif
Sans Serif

Requirements
Must have
• Venture Brightpath by Marlon Tibbet
Nice to have
• About, plans to buy, why health and wellness is important. (exsposure to subnlight, ice baht, sauna, daily movement, whole foods)

```html
<!DOCTYPE html>
<html lang="en">
<head>
<meta charset="UTF-8">
<title>Venture Brightpath by Marlon Tibbet</title>
<link href="https://fonts.googleapis.com/css2?family=Jost:wght@400;500;600&family=Poppins:ital,wght@1,800&display=swap" rel="stylesheet">
<style>
  :root {
    --red: #e3141f;
    --red-faint: rgba(150, 14, 20, 0.38);
    --ink: #0c0c0c;
    --white: #ffffff;
    --text-soft: #f1f1f1;
  }
  * { margin: 0; padding: 0; box-sizing: border-box; }
  html, body { width: 1200px; height: 675px; overflow: hidden; background: var(--ink); }
  .hero {
    position: relative;
    width: 1200px;
    height: 675px;
    overflow: hidden;
    background:
      radial-gradient(ellipse at 75% 40%, #2a2a2a 0%, #161616 45%, #0a0a0a 100%);
    font-family: "Jost", sans-serif;
  }
  .hero-backword {
    position: absolute;
    left: 10px;
    top: 232px;
    font-family: "Jost", sans-serif;
    font-weight: 600;
    font-size: 168px;
    letter-spacing: 4px;
    color: var(--red-faint);
    white-space: nowrap;
    line-height: 1;
  }
  .hero-photo {
    position: absolute;
    left: 615px;
    top: 112px;
    width: 390px;
    height: 563px;
    border-radius: 160px 160px 20px 20px;
    background: linear-gradient(180deg, #3a2a22 0%, #7a5440 30%, #5b3e2f 60%, #151515 85%, #0e0e0e 100%);
    opacity: 0.9;
  }
  .brand {
    position: absolute;
    left: 96px;
    top: 92px;
  }
  .brand-name {
    font-family: "Jost", sans-serif;
    font-weight: 600;
    font-size: 38px;
    line-height: 1;
    color: var(--red);
    text-transform: uppercase;
    letter-spacing: 1px;
  }
  .brand-byline {
    margin-top: 10px;
    margin-left: 90px;
    font-family: "Jost", sans-serif;
    font-weight: 600;
    font-size: 21px;
    color: var(--white);
  }
  .headline {
    position: absolute;
    left: 84px;
    top: 232px;
    font-weight: 500;
    font-size: 71px;
    line-height: 64px;
    color: var(--white);
  }
  .headline .accent { color: var(--red); display: block; }
  .lead {
    position: absolute;
    left: 85px;
    top: 380px;
    font-weight: 400;
    font-size: 21px;
    line-height: 27px;
    color: var(--text-soft);
  }
  .lead .lead-brand { color: var(--red); font-weight: 600; }
  .actions {
    position: absolute;
    left: 84px;
    top: 461px;
    width: 410px;
    height: 58px;
  }
  .actions svg { position: absolute; left: 0; top: 0; }
  .btn {
    position: absolute;
    top: 0;
    height: 58px;
    display: flex;
    align-items: center;
    justify-content: center;
    font-family: "Poppins", sans-serif;
    font-style: italic;
    font-weight: 800;
    font-size: 17px;
    text-decoration: none;
    letter-spacing: 0.3px;
  }
  .btn-primary { left: 6px; width: 190px; color: var(--white); }
  .btn-secondary { left: 198px; width: 200px; color: var(--red); }
</style>
</head>
<body>
  <section class="hero">
    <div class="hero-backword" aria-hidden="true">BRIGHTPATH</div>
    <div class="hero-photo" role="img" aria-label="Photo of the coach standing shirtless in a dark gym"></div>

    <div class="brand">
      <div class="brand-name">Venture Brightpath</div>
      <div class="brand-byline">by Marlon Tibbet</div>
    </div>

    <h1 class="headline">Unleash Your<span class="accent">Limitless Potential</span></h1>

    <p class="lead">Redefine Your Limits, Push Beyond Boundaries and<br>Achieve the Ultimate with <span class="lead-brand">Venture Brightpath</span></p>

    <div class="actions">
      <svg width="410" height="58" viewBox="0 0 410 58" aria-hidden="true">
        <polygon points="20,1 207,1 188,57 1,57" fill="none" stroke="#e3141f" stroke-width="2"/>
        <polygon points="25,6 200,6 184,52 9,52" fill="#e3141f"/>
        <polygon points="217,1 408,1 389,57 198,57" fill="none" stroke="#e3141f" stroke-width="2.5"/>
      </svg>
      <a class="btn btn-primary" href="#plans">GET STARTED</a>
      <a class="btn btn-secondary" href="#about">LEARN MORE</a>
    </div>
  </section>
</body>
</html>
```